Flyer for local business that installs fences and sells fence materials

We recently began selling fence materials, in addition to also doing fence installations. We need a flyer that displays our business information and photos of our work, as well as a flyer that shows customers they have the option to buy materials only also.

If they are looking to build a fence - we can help by installing it, or if they want to install themselves, they can buy the materials only from us too. We provide a lifetime warranty on all materials and installations. More information about the company is here: www.BrambleRailWorks.com

Its important to have the company logo, phone number, email and business hours listed (Monday - Thursday 9AM - 3PM, Friday 9AM - 1PM).

It is also important to show the fence material types we offer:
Wood, Chainlink, Vinyl and Aluminum
Updates

Updated with more photos and url to website www.bramblerailworks.com for details

Target Market(s)

Residential Homeowners

Industry/Entity Type

Construction

Font styles to use
Sans Serif
Other font styles liked:
• Arial

Colors
0054AA
0677BA
7BADD7
CADEEF
E8F1F8

Requirements
Must have
• Photos of the fencing we offer
Nice to have
• A way to explain to customers they can hire us to install, or just buy the materials from us
Should not have
• Too many colors or too many words

```html
<!DOCTYPE html>
<html lang="en">
<head>
<meta charset="utf-8">
<title>Bramble Rail Works – Install or Buy Materials</title>
<link rel="stylesheet" href="https://fonts.googleapis.com/css2?family=Bebas+Neue&family=Montserrat:wght@300;600;800&family=Russo+One&display=swap">
<style>
  :root {
    --sky-pale: #e8f1f8;
    --sky-soft: #cadeef;
    --sky-mid: #7badd7;
    --wood-light: #e6c46a;
    --wood-mid: #d6a548;
    --wood-deep: #b57d2c;
    --ink: #111111;
    --paper: #ffffff;
    --brown: #6b4215;
  }
  * { margin: 0; padding: 0; box-sizing: border-box; }
  html, body { width: 848px; height: 1200px; overflow: hidden; background: #ffffff; }
  .flyer {
    position: relative;
    width: 848px;
    height: 1200px;
    overflow: hidden;
    font-family: "Montserrat", Arial, sans-serif;
  }
  .backdrop {
    position: absolute;
    inset: 0;
    background: linear-gradient(172deg,
      var(--sky-pale) 0%,
      var(--sky-soft) 12%,
      var(--sky-mid) 25%,
      var(--wood-light) 42%,
      var(--wood-mid) 68%,
      var(--wood-deep) 100%);
  }

  .brand {
    position: absolute;
    left: 506px;
    top: 36px;
    width: 316px;
    color: var(--ink);
  }
  .brand-row { display: flex; align-items: center; gap: 12px; }
  .brand-mark { width: 58px; height: 82px; background: var(--ink); flex: none; }
  .brand-name {
    font-family: "Russo One", Arial, sans-serif;
    font-size: 20px;
    line-height: 1.2;
    white-space: nowrap;
  }
  .brand-phone {
    font-family: "Russo One", Arial, sans-serif;
    font-size: 25px;
    line-height: 1.15;
    white-space: nowrap;
  }
  .brand-tagline {
    font-family: "Russo One", Arial, sans-serif;
    font-size: 7.6px;
    margin-top: 4px;
    white-space: nowrap;
  }

  .contact {
    position: absolute;
    left: 506px;
    top: 146px;
    width: 306px;
    color: var(--ink);
    text-align: center;
    font-weight: 300;
  }
  .contact-email {
    font-size: 19px;
    padding-bottom: 6px;
    border-bottom: 1px solid var(--ink);
    letter-spacing: 0.3px;
  }
  .contact-hours { font-size: 18.5px; line-height: 24px; margin-top: 6px; letter-spacing: 0.3px; }
  .contact-web { font-size: 15px; font-weight: 600; margin-top: 10px; }
  .contact-warranty { font-size: 13px; font-weight: 600; margin-top: 4px; }

  .gallery { position: absolute; left: 92px; top: 226px; width: 320px; height: 960px; }
  .snapshot {
    position: absolute;
    left: 0;
    width: 162px;
    background: var(--paper);
    padding: 10px;
    transform: skewY(-10deg);
    transform-origin: left top;
    box-shadow: 6px 10px 14px rgba(60, 35, 0, 0.35);
  }
  .snapshot-image { width: 100%; height: 100%; }
  .snapshot-aluminum { top: 28px; height: 208px; }
  .snapshot-aluminum .snapshot-image { background: linear-gradient(180deg, #cfd9cf 0%, #6f8a4c 40%, #3a4a25 60%, #8ea458 100%); }
  .snapshot-chainlink { top: 268px; height: 206px; }
  .snapshot-chainlink .snapshot-image { background: linear-gradient(180deg, #5f7a3a 0%, #b8c2b3 35%, #7e934a 65%, #556b2c 100%); }
  .snapshot-vinyl { top: 510px; height: 196px; }
  .snapshot-vinyl .snapshot-image { background: linear-gradient(180deg, #2d5fa8 0%, #6e8fb8 28%, #f1f1ef 45%, #cfcfcf 75%, #5a4a30 100%); }
  .snapshot-wood { top: 750px; height: 192px; }
  .snapshot-wood .snapshot-image { background: linear-gradient(180deg, #5a6f3a 0%, #c3b9ad 25%, #9c8a76 60%, #3c3c3c 100%); }

  .material-label {
    position: absolute;
    left: 176px;
    font-family: "Bebas Neue", Arial, sans-serif;
    font-size: 30px;
    line-height: 1;
    color: var(--paper);
    letter-spacing: 1px;
  }
  .label-aluminum { top: 110px; }
  .label-chainlink { top: 350px; }
  .label-vinyl { top: 590px; }
  .label-wood { top: 830px; }

  .headline {
    position: absolute;
    right: 38px;
    font-family: "Bebas Neue", Arial, sans-serif;
    color: var(--paper);
    font-size: 90px;
    line-height: 1;
    text-align: right;
    letter-spacing: 0.5px;
    font-weight: 400;
    white-space: nowrap;
  }
  .headline-1 { top: 647px; }
  .headline-2 { top: 735px; }
  .headline-4 { top: 913px; }
  .headline-5 { top: 1002px; }
  .headline-6 { top: 1090px; }
  .choice {
    position: absolute;
    left: 682px;
    top: 827px;
    width: 127px;
    height: 68px;
    background: var(--paper);
    color: var(--brown);
    font-family: "Montserrat", Arial, sans-serif;
    font-weight: 800;
    font-size: 48px;
    line-height: 68px;
    text-align: center;
  }
</style>
</head>
<body>
<main class="flyer">
  <div class="backdrop" role="img" aria-label="Photo of a tall pine privacy fence under a bright blue sky"></div>

  <header class="brand">
    <div class="brand-row">
      <span class="brand-mark" aria-hidden="true"></span>
      <div>
        <div class="brand-name">Bramble Rail Works</div>
        <div class="brand-phone">704-555-0186</div>
        <div class="brand-tagline">“Because Good Fences Make Good Neighbors”</div>
      </div>
    </div>
  </header>

  <section class="contact">
    <p class="contact-email">office@bramblerailworks.com</p>
    <p class="contact-hours">Monday - Thursday 9AM - 3PM,<br>Friday 9AM - 1PM</p>
    <p class="contact-web">www.bramblerailworks.com</p>
    <p class="contact-warranty">Lifetime warranty on all materials &amp; installs</p>
  </section>

  <section class="gallery">
    <figure class="snapshot snapshot-aluminum"><div class="snapshot-image" role="img" aria-label="Photo of a black aluminum fence on a grassy slope"></div></figure>
    <span class="material-label label-aluminum">Aluminum</span>
    <figure class="snapshot snapshot-chainlink"><div class="snapshot-image" role="img" aria-label="Photo of a chainlink fence along a backyard"></div></figure>
    <span class="material-label label-chainlink">Chainlink</span>
    <figure class="snapshot snapshot-vinyl"><div class="snapshot-image" role="img" aria-label="Photo of a white vinyl privacy fence"></div></figure>
    <span class="material-label label-vinyl">Vinyl</span>
    <figure class="snapshot snapshot-wood"><div class="snapshot-image" role="img" aria-label="Photo of wrapped pallets of wood fence materials"></div></figure>
    <span class="material-label label-wood">Wood</span>
  </section>

  <h1>
    <span class="headline headline-1">Hire us</span>
    <span class="headline headline-2">to install</span>
    <span class="choice">OR</span>
    <span class="headline headline-4">buy the</span>
    <span class="headline headline-5">materials</span>
    <span class="headline headline-6">from us</span>
  </h1>
</main>
</body>
</html>
```